Order Management User Interface

I need a new design for our order management screens. They need to be end user friendly and contain the data in an easy to read format. These are online orders. I have attached 3 images from the development solution. For now I just need a new UI and ideally would like it delivered in html so we can easily adapt. The screen has multiple tabs to display the different types of data we store. Ideally the end user needs to see customer focused information first.
I have uploaded an example of a different order view that i like.
Fashion Retail
Coded - Design and coding required
1 page

```html
<!DOCTYPE html>
<html lang="en">
<head>
<meta charset="utf-8">
<title>Order BSDHUISD – Liam Carter</title>
<link href="https://fonts.googleapis.com/css2?family=Poppins:wght@300;400;500;600&display=swap" rel="stylesheet">
<style>
:root{
  --navy:#0a1b2d;
  --navy-2:#1b2b3f;
  --blue:#0a71ad;
  --blue-dark:#07639a;
  --cyan:#21b6ea;
  --ice:#eaf5fb;
  --ice-2:#d8eef9;
  --page:#f4f6f9;
  --white:#ffffff;
  --ink:#1a1f2b;
  --muted:#8a93a0;
  --line:#cfd6de;
  --green:#27c25f;
  --red:#ef2b2b;
  --yellow:#f7c30a;
  --magenta:#d21be8;
  --purple:#7a10e0;
  --accent-blue:#0d6ff0;
}
*{box-sizing:border-box;margin:0;padding:0}
html,body{width:1200px;height:1006px;overflow:hidden;background:var(--page)}
body{font-family:'Poppins',sans-serif;color:var(--ink)}
.screen{position:relative;width:2100px;height:1760px;transform:scale(.571428);transform-origin:0 0;background:var(--page);overflow:hidden}
.a{position:absolute}
svg{display:block}

/* top bar */
.topbar{left:0;top:0;width:2100px;height:71px;background:var(--navy);color:var(--white)}
.brand{left:64px;top:22px;font-size:21px;font-weight:500}
.page-title{left:292px;top:20px;font-size:20px;font-weight:500}
.search{left:1414px;top:16px;width:385px;height:40px;border:1px solid #3b4a5c;border-radius:3px;color:#7d8896;font-size:15px;padding:9px 12px}
.search svg{position:absolute;right:14px;top:11px}
.avatar{left:1844px;top:21px;width:28px;height:28px;border-radius:50%;background:linear-gradient(135deg,#9aa3ad,#4d5864)}
.user{left:1878px;top:16px;font-size:16px;font-weight:500;line-height:20px}
.user small{display:block;font-size:11px;font-weight:400}

/* sidebar */
.sidebar{left:0;top:71px;width:238px;height:1110px;background:var(--navy);color:#8894a3}
.nav-active{position:absolute;left:0;top:34px;width:238px;height:48px;background:var(--navy-2)}
.nav-item{position:absolute;left:38px;font-size:21px;font-weight:300;display:flex;align-items:center;gap:12px}
.nav-item svg{width:22px;height:22px}
.nav-sub{position:absolute;left:72px;font-size:16px;font-weight:300}
.caret{position:absolute;left:212px;width:0;height:0;border-left:5px solid transparent;border-right:5px solid transparent}

/* cards */
.card{background:var(--white);border-radius:10px}
.stat-icon{width:57px;height:57px;border-radius:50%;display:flex;align-items:center;justify-content:center;color:var(--white);font-size:28px;font-weight:600}
.stat-bar{width:3px;height:72px}
.stat-label{font-size:20px;font-weight:400}
.stat-value{font-size:25px;font-weight:400}

.panel-head{background:var(--blue);color:var(--white);height:57px;border-radius:10px 10px 0 0;display:flex;align-items:center;padding-left:31px;gap:14px;font-size:21px;font-weight:500}
.chip{background:var(--blue-dark);padding:6px 17px;border-radius:3px;font-weight:400}
.btn-w{position:absolute;top:8px;height:40px;background:var(--white);color:var(--blue);border-radius:3px;font-size:16px;display:flex;align-items:center;justify-content:center;gap:6px}

.tab{position:absolute;height:44px;display:flex;align-items:center;gap:7px;font-size:18px;padding:0 15px;border:1px solid var(--line)}
.tab.on{background:var(--white);border-bottom-color:var(--white);color:var(--ink)}
.tab.off{background:#f6f8fa;color:#a7aeb8}
.badge{width:22px;height:22px;border-radius:50%;background:var(--blue);color:var(--white);font-size:12px;display:flex;align-items:center;justify-content:center}
.tab.off .badge{background:#cfd6de}
.box{position:absolute;border:1px solid var(--line);background:var(--white)}
.btn-o{position:absolute;height:33px;border:1px solid #b9c1ca;border-radius:3px;background:var(--white);font-size:16px;display:flex;align-items:center;justify-content:center;gap:6px}
.t15{font-size:15px}
.tag{position:absolute;top:844px;height:34px;background:var(--ice);font-size:16px;display:flex;align-items:center;gap:8px;padding:0 13px}

.field{position:absolute;left:1253px;border-left:2px solid #2b3440;padding-left:10px;font-size:15px;line-height:27px}
.field span{color:#6b7480;font-weight:300}

/* calendar */
.cal{left:1812px;top:850px;width:235px;height:215px;background:var(--white);box-shadow:0 3px 14px rgba(0,0,0,.12);font-size:9px;font-weight:500}
.cal .d{position:absolute;width:22px;text-align:center}
.cal .x{color:#c8cdd3}
.cal .sel{background:var(--blue);color:var(--white);border-radius:50%;height:20px;line-height:20px;top:-5px}

/* purchased items */
.tabs-bar{left:262px;top:1065px;width:1814px;height:57px;background:var(--blue);border-radius:10px 10px 0 0;color:var(--white)}
.ptab{position:absolute;top:0;height:57px;display:flex;align-items:center;justify-content:center;font-size:16px;border-right:1px solid #2a86bd}
.ptab.on{background:var(--cyan)}
.sel-box{position:absolute;top:9px;height:39px;border:1px solid #9bcbe6;border-radius:3px;font-size:16px;display:flex;align-items:center;padding:0 12px;gap:9px}
.thead{left:292px;top:1145px;width:1754px;height:45px;background:var(--blue);border-radius:3px;color:var(--white);font-size:15px;font-weight:500}
.th{position:absolute;top:13px}
.row{position:absolute;left:292px;width:1754px;height:86px;border-bottom:1px solid #d7dde3;font-size:16px;font-weight:600}
.row.hl{background:var(--ice)}
.td{position:absolute;top:22px;line-height:22px}
.pid{color:var(--cyan)}
.dash{font-weight:400;color:#555}
.pill{position:absolute;left:1339px;top:29px;width:103px;height:35px;border-radius:10px;color:var(--white);font-size:16px;font-weight:500;display:flex;align-items:center;justify-content:center}
.dots{position:absolute;left:1734px;top:27px}
.menu{background:var(--white);box-shadow:0 3px 12px rgba(0,0,0,.12);font-size:17px}
.menu div{height:35px;line-height:35px;padding-left:18px}
.menu .hov{background:#f1f5f8}
</style>
</head>
<body>
<div class="screen">

  <!-- top bar -->
  <header class="a topbar">
    <div class="a brand">Dashboard</div>
    <div class="a page-title">Order BSDHUISD – Liam Carter</div>
    <div class="a search">Search here
      <svg width="17" height="17" viewBox="0 0 17 17" fill="none" stroke="#9aa4b0" stroke-width="1.6"><circle cx="7" cy="7" r="5.5"/><path d="M11 11l5 5"/></svg>
    </div>
    <div class="a avatar" role="img" aria-label="User profile photo"></div>
    <div class="a user">Nora Bell<small>Admin</small></div>
    <svg class="a" style="left:2002px;top:26px" width="12" height="8" viewBox="0 0 12 8" fill="none" stroke="#fff" stroke-width="1.6"><path d="M1 1l5 5 5-5"/></svg>
  </header>

  <!-- sidebar -->
  <nav class="a sidebar">
    <div class="nav-active"></div>
    <div class="nav-item" style="top:45px;color:#c8d0da">
      <svg viewBox="0 0 22 22" fill="none" stroke="currentColor" stroke-width="1.5"><path d="M2 10L11 2l9 8v10h-6v-6H8v6H2z"/></svg>Orders</div>
    <div class="caret" style="top:56px;border-bottom:6px solid #fff"></div>
    <div class="nav-sub" style="top:98px;color:#fff;font-weight:500">Orders</div>
    <div class="nav-sub" style="top:133px">Invoices</div>
    <div class="nav-sub" style="top:168px">Lorem</div>
    <div class="nav-sub" style="top:203px">Lorem ipsum</div>
    <div class="nav-sub" style="top:238px">Lorem ipsum</div>
    <div class="nav-sub" style="top:273px">Lorem ipsum</div>
    <div class="nav-sub" style="top:308px">Lorem ipsum</div>
    <div class="nav-sub" style="top:343px">Lorem</div>

    <div class="nav-item" style="top:387px"><svg viewBox="0 0 22 22" fill="none" stroke="currentColor" stroke-width="1.5"><circle cx="11" cy="11" r="9"/><circle cx="11" cy="11" r="4"/></svg>Lorem</div>
    <div class="caret" style="top:399px;border-top:6px solid #8894a3"></div>
    <div class="nav-item" style="top:436px"><svg viewBox="0 0 22 22" fill="none" stroke="currentColor" stroke-width="1.5"><path d="M11 2l3 3h4v4l3 2-3 2v4h-4l-3 3-3-3H4v-4l-3-2 3-2V5h4z"/></svg>Lorem</div>
    <div class="caret" style="top:448px;border-top:6px solid #8894a3"></div>
    <div class="nav-item" style="top:485px"><svg viewBox="0 0 22 22" fill="none" stroke="currentColor" stroke-width="1.5"><circle cx="11" cy="11" r="9"/><circle cx="11" cy="11" r="3"/></svg>Lorem</div>
    <div class="nav-item" style="top:535px"><svg viewBox="0 0 22 22" fill="none" stroke="currentColor" stroke-width="1.5"><rect x="3" y="2" width="16" height="18" rx="2"/><path d="M7 7h8M7 11h8M7 15h5"/></svg>Lorem ipsum</div>
    <div class="nav-item" style="top:584px"><svg viewBox="0 0 22 22" fill="none" stroke="currentColor" stroke-width="1.5"><circle cx="5" cy="5" r="3"/><circle cx="17" cy="5" r="3"/><circle cx="5" cy="17" r="3"/><circle cx="17" cy="17" r="3"/><path d="M8 5h6M8 17h6"/></svg>Lorem</div>
    <div class="nav-item" style="top:633px"><svg viewBox="0 0 22 22" fill="none" stroke="currentColor" stroke-width="1.5"><circle cx="11" cy="11" r="9"/><path d="M7 11l3 3 5-6"/></svg>Lorem</div>
    <div class="nav-item" style="top:682px"><svg viewBox="0 0 22 22" fill="none" stroke="currentColor" stroke-width="1.5"><path d="M5 16V9a6 6 0 0112 0v7l2 2H3zM9 20h4"/></svg>Lorem ipsum</div>
    <div class="nav-item" style="top:731px"><svg viewBox="0 0 22 22" fill="none" stroke="currentColor" stroke-width="1.5"><circle cx="11" cy="5" r="3"/><circle cx="4" cy="18" r="2.5"/><circle cx="18" cy="18" r="2.5"/><path d="M9 8l-4 8M13 8l4 8M7 18h8"/></svg>Lorem ipsum</div>
  </nav>

  <!-- summary stats -->
  <section class="a card" style="left:260px;top:97px;width:1815px;height:150px">
    <div class="a stat-icon" style="left:29px;top:47px;background:var(--accent-blue)"><svg width="26" height="26" viewBox="0 0 26 26" fill="none" stroke="#fff" stroke-width="2"><rect x="3" y="5" width="20" height="18" rx="2"/><path d="M3 11h20M8 2v5M18 2v5"/></svg></div>
    <div class="a stat-bar" style="left:104px;top:42px;background:var(--accent-blue)"></div>
    <div class="a stat-label" style="left:126px;top:38px">Date</div><div class="a stat-value" style="left:126px;top:80px">01/01/2022</div>

    <div class="a stat-icon" style="left:368px;top:47px;background:var(--yellow)">€</div>
    <div class="a stat-bar" style="left:444px;top:42px;background:var(--yellow)"></div>
    <div class="a stat-label" style="left:466px;top:38px">Total</div><div class="a stat-value" style="left:466px;top:80px">€50.00</div>

    <div class="a stat-icon" style="left:667px;top:47px;background:var(--green)"><svg width="26" height="26" viewBox="0 0 26 26" fill="none" stroke="#fff" stroke-width="2"><path d="M3 4h20v14H9l-6 5z"/></svg></div>
    <div class="a stat-bar" style="left:742px;top:42px;background:var(--green)"></div>
    <div class="a stat-label" style="left:764px;top:38px">Message</div><div class="a stat-value" style="left:764px;top:80px">NA</div>

    <div class="a stat-icon" style="left:967px;top:47px;background:var(--red)"><svg width="24" height="26" viewBox="0 0 24 26" fill="none" stroke="#fff" stroke-width="2"><path d="M4 2h11l6 6v16H4z"/><path d="M8 12h9M8 16h9M8 20h6"/></svg></div>
    <div class="a stat-bar" style="left:1042px;top:42px;background:var(--red)"></div>
    <div class="a stat-label" style="left:1064px;top:38px">Products</div><div class="a stat-value" style="left:1064px;top:80px">23</div>

    <div class="a stat-icon" style="left:1265px;top:47px;background:var(--magenta)"><svg width="26" height="26" viewBox="0 0 26 26" fill="none" stroke="#fff" stroke-width="2"><rect x="3" y="5" width="20" height="18" rx="2"/><path d="M3 11h20M8 2v5M18 2v5"/></svg></div>
    <div class="a stat-bar" style="left:1340px;top:42px;background:var(--magenta)"></div>
    <div class="a stat-label" style="left:1362px;top:38px">Date</div><div class="a stat-value" style="left:1362px;top:80px">01/01/2022</div>

    <div class="a stat-icon" style="left:1605px;top:47px;background:var(--purple)">€</div>
    <div class="a stat-bar" style="left:1680px;top:42px;background:var(--purple)"></div>
    <div class="a stat-label" style="left:1702px;top:38px">Total</div><div class="a stat-value" style="left:1702px;top:80px">€50.00</div>
  </section>

  <!-- order panel -->
  <section class="a card" style="left:260px;top:279px;width:893px;height:755px">
    <div class="panel-head">Order <span class="chip">BSDHUISD</span><span class="chip">#15</span></div>
    <div class="btn-w" style="left:659px;width:97px">Back <svg width="18" height="14" viewBox="0 0 18 14" fill="none" stroke="currentColor" stroke-width="2"><path d="M8 1L2 7l6 6M16 1l-6 6 6 6"/></svg></div>
    <div class="btn-w" style="left:767px;width:97px"><svg width="18" height="14" viewBox="0 0 18 14" fill="none" stroke="currentColor" stroke-width="2"><path d="M2 1l6 6-6 6M10 1l6 6-6 6"/></svg> Next</div>
  </section>

  <div class="box" style="left:292px;top:413px;width:833px;height:221px"></div>
  <div class="tab on" style="left:292px;top:370px;width:146px"><svg width="18" height="18" viewBox="0 0 18 18" fill="none" stroke="#222" stroke-width="1.5"><circle cx="9" cy="9" r="7.5"/><path d="M9 4v5l-3 2"/></svg>Status<span class="badge">1</span></div>
  <div class="tab off" style="left:437px;top:370px;width:194px"><svg width="15" height="17" viewBox="0 0 15 17" fill="none" stroke="#a7aeb8" stroke-width="1.5"><path d="M2 1h8l4 4v11H2z"/><path d="M5 9h6M5 12h6"/></svg>Documents<span class="badge">1</span></div>
  <div class="a" style="left:310px;top:436px;width:785px;height:45px;background:var(--ice)"></div>
  <svg class="a" style="left:328px;top:449px" width="20" height="20" viewBox="0 0 20 20"><circle cx="10" cy="10" r="10" fill="#27c25f"/><path d="M5.5 10.5l3 3 6-6.5" stroke="#fff" stroke-width="2" fill="none"/></svg>
  <div class="a t15" style="left:354px;top:449px;font-size:16px">Payment Accepted</div>
  <div class="a t15" style="left:665px;top:449px">01/24/2022 | 10:12:35</div>
  <div class="btn-o" style="left:933px;top:442px;width:149px"><svg width="20" height="15" viewBox="0 0 20 15" fill="none" stroke="#222" stroke-width="1.5"><rect x="1" y="1" width="18" height="13"/><path d="M1 1l9 7 9-7"/></svg>Resend Mail</div>
  <div class="btn-o" style="left:354px;top:502px;width:259px;justify-content:space-between;padding:0 16px">Payment Accepted<svg width="10" height="6" viewBox="0 0 10 6"><path d="M0 0h10L5 6z" fill="#222"/></svg></div>
  <div class="btn-o" style="left:629px;top:502px;width:149px">Update Status</div>
  <div class="a" style="left:310px;top:552px;width:785px;height:1px;background:#e1e5ea"></div>
  <div class="btn-o" style="left:797px;top:571px;width:135px"><svg width="17" height="16" viewBox="0 0 17 16" fill="none" stroke="#222" stroke-width="1.5"><path d="M4 5V1h9v4M4 12H1V5h15v7h-3M4 9h9v6H4z"/></svg>Print Order</div>
  <div class="btn-o" style="left:947px;top:571px;width:135px"><svg width="17" height="16" viewBox="0 0 17 16" fill="none" stroke="#222" stroke-width="1.5"><path d="M4 5V1h9v4M4 12H1V5h15v7h-3M4 9h9v6H4z"/></svg>View invoice</div>

  <div class="box" style="left:292px;top:721px;width:833px;height:178px"></div>
  <div class="tab on" style="left:292px;top:678px;width:167px"><svg width="22" height="17" viewBox="0 0 22 17" fill="#222"><path d="M8 1h13v11H8zM1 6l3-4h3v10H1z"/><circle cx="5" cy="14" r="2.5"/><circle cx="16" cy="14" r="2.5"/></svg>Shipping<span class="badge">1</span></div>
  <div class="tab off" style="left:458px;top:678px;width:272px"><svg width="15" height="17" viewBox="0 0 15 17" fill="none" stroke="#a7aeb8" stroke-width="1.5"><path d="M2 1h8l4 4v11H2z"/><path d="M5 9h6M5 12h6"/></svg>Merchandise Returns<span class="badge">0</span></div>
  <div class="a" style="left:310px;top:744px;width:785px;height:45px;background:var(--ice)"></div>
  <div class="a t15" style="left:328px;top:758px;color:#555">Date</div>
  <div class="a t15" style="left:497px;top:758px;color:#555">Carrier</div>
  <div class="a t15" style="left:600px;top:758px;color:#555">Weight</div>
  <div class="a t15" style="left:692px;top:758px;color:#555">Shipping Cost</div>
  <div class="a t15" style="left:831px;top:758px;color:#555">Tracking number</div>
  <div class="a t15" style="left:328px;top:802px">01/24/2022 | 10:12:35</div>
  <div class="a t15" style="left:497px;top:802px">My carrier</div>
  <div class="a t15" style="left:600px;top:802px">0.00 kg</div>
  <div class="a t15" style="left:692px;top:802px">€50.00</div>
  <div class="a t15" style="left:831px;top:802px">SA455SDD4SD41D</div>
  <div class="a t15" style="left:1027px;top:802px;color:var(--cyan);text-decoration:underline;display:flex;gap:6px"><svg width="16" height="16" viewBox="0 0 16 16" fill="none" stroke="#21b6ea" stroke-width="1.4"><path d="M2 14l1-4 8-8 3 3-8 8zM1 15h14"/></svg>Edit</div>
  <div class="tag" style="left:328px">Recycled packaging <b style="font-size:20px">✖</b></div>
  <div class="tag" style="left:529px">Gift Wrapping <b style="font-size:20px">✖</b></div>

  <!-- customer panel -->
  <section class="a card" style="left:1183px;top:279px;width:893px;height:755px">
    <div class="panel-head">Customer <span class="chip">Liam Carter</span><span class="chip">#25</span></div>
    <div class="btn-w" style="left:698px;width:162px">View full details</div>
  </section>
  <div class="a" style="left:1215px;top:364px;width:828px;height:356px;background:var(--ice)"></div>
  <div class="field" style="top:382px"><span>Email</span><br>liam.carter@mailbox.test</div>
  <div class="field" style="top:448px"><span>Account Registered</span><br>01/24/2022 | 10:12:35</div>
  <div class="field" style="top:514px"><span>Valid order placed</span><br>4</div>
  <div class="field" style="top:579px"><span>Total spent</span><br>€50.00</div>
  <div class="a" style="left:1596px;top:385px;font-size:15px;color:#6b7480;font-weight:300">Private Note:</div>
  <div class="a" style="left:1594px;top:414px;width:418px;height:215px;background:var(--ice-2);border:1px solid #bcdcee;padding:12px 15px;font-size:15px;color:#6b7480;font-weight:300">Write here</div>
  <div class="a" style="left:1915px;top:652px;width:97px;height:41px;background:var(--cyan);border-radius:3px;color:#fff;font-size:16px;display:flex;align-items:center;justify-content:center;gap:7px"><svg width="18" height="18" viewBox="0 0 18 18" fill="#fff"><path d="M1 1h13l3 3v13H1z"/><rect x="4" y="2" width="8" height="5" fill="#21b6ea"/><rect x="4" y="10" width="10" height="6" fill="#21b6ea"/></svg>Save</div>

  <div class="box" style="left:1215px;top:800px;width:832px;height:207px"></div>
  <div class="tab on" style="left:1215px;top:757px;width:213px"><svg width="22" height="17" viewBox="0 0 22 17" fill="#222"><path d="M8 1h13v11H8zM1 6l3-4h3v10H1z"/><circle cx="5" cy="14" r="2.5"/><circle cx="16" cy="14" r="2.5"/></svg>Shipping Address</div>
  <div class="tab off" style="left:1427px;top:757px;width:195px"><svg width="15" height="17" viewBox="0 0 15 17" fill="none" stroke="#a7aeb8" stroke-width="1.5"><path d="M2 1h8l4 4v11H2z"/><path d="M5 9h6M5 12h6"/></svg>Invoice Address</div>
  <div class="a" style="left:1233px;top:823px;width:785px;height:163px;background:var(--ice)"></div>
  <div class="a" style="left:1253px;top:838px;font-size:15px;line-height:22px;color:#4a5260;font-weight:300">21 Street,<br>Lorem ipsum dolor<br>amet, consetetur<br>sadipscing elitr, sed<br>France<br>0612345678</div>
  <div class="a" style="left:1948px;top:838px;font-size:14px;color:#b7dff2">✎ Edit</div>

  <!-- date picker -->
  <div class="a cal">
    <div class="d" style="left:32px;top:13px">«</div><div class="d" style="left:52px;top:13px">‹</div>
    <div class="a" style="left:86px;top:13px">18 Apr 2022</div>
    <div class="d" style="left:159px;top:13px">›</div><div class="d" style="left:179px;top:13px">»</div>
    <div class="d" style="left:17px;top:41px">Su</div><div class="d" style="left:47px;top:41px">Mo</div><div class="d" style="left:78px;top:41px">Tu</div><div class="d" style="left:108px;top:41px">We</div><div class="d" style="left:139px;top:41px">Th</div><div class="d" style="left:169px;top:41px">Fr</div><div class="d" style="left:198px;top:41px">Sa</div>
    <div class="d x" style="left:17px;top:64px">25</div><div class="d x" style="left:47px;top:64px">26</div><div class="d x" style="left:78px;top:64px">27</div><div class="d x" style="left:108px;top:64px">28</div><div class="d x" style="left:139px;top:64px">29</div><div class="d x" style="left:169px;top:64px">30</div><div class="d" style="left:198px;top:64px">1</div>
    <div class="d" style="left:17px;top:90px">2</div><div class="d" style="left:47px;top:90px">3</div><div class="d" style="left:78px;top:90px">4</div><div class="d" style="left:108px;top:90px">5</div><div class="d" style="left:139px;top:90px">6</div><div class="d" style="left:169px;top:90px">7</div><div class="d" style="left:198px;top:90px">8</div>
    <div class="d" style="left:17px;top:117px">9</div><div class="d" style="left:47px;top:117px"><div class="d sel" style="left:0">10</div></div><div class="d" style="left:78px;top:117px">11</div><div class="d" style="left:108px;top:117px">12</div><div class="d" style="left:139px;top:117px">13</div><div class="d" style="left:169px;top:117px">14</div><div class="d" style="left:198px;top:117px">15</div>
    <div class="d" style="left:17px;top:144px">16</div><div class="d" style="left:47px;top:144px">17</div><div class="d" style="left:78px;top:144px">18</div><div class="d" style="left:108px;top:144px">19</div><div class="d" style="left:139px;top:144px">20</div><div class="d" style="left:169px;top:144px">21</div><div class="d" style="left:198px;top:144px">22</div>
    <div class="d" style="left:17px;top:171px">23</div><div class="d" style="left:47px;top:171px">24</div><div class="d" style="left:78px;top:171px">25</div><div class="d" style="left:108px;top:171px">26</div><div class="d" style="left:139px;top:171px">27</div><div class="d" style="left:169px;top:171px">28</div><div class="d" style="left:198px;top:171px">29</div>
    <div class="d" style="left:17px;top:197px">30</div><div class="d" style="left:47px;top:197px">31</div><div class="d x" style="left:78px;top:197px">1</div><div class="d x" style="left:108px;top:197px">2</div><div class="d x" style="left:139px;top:197px">3</div><div class="d x" style="left:169px;top:197px">4</div><div class="d x" style="left:198px;top:197px">5</div>
  </div>

  <!-- purchased items -->
  <section class="a card" style="left:262px;top:1065px;width:1814px;height:497px;border-radius:10px"></section>
  <div class="a tabs-bar">
    <div class="ptab on" style="left:0;width:154px;border-radius:10px 0 0 0">Purchased Items</div>
    <div class="ptab" style="left:154px;width:107px">Payment</div>
    <div class="ptab" style="left:261px;width:88px">History</div>
    <div class="ptab" style="left:349px;width:107px">Vouchers</div>
    <div class="ptab" style="left:456px;width:79px">Other</div>
    <div class="ptab" style="left:535px;width:85px">Others</div>
    <div class="a" style="left:1243px;top:15px;font-size:20px;font-weight:500">Filters</div>
    <div class="sel-box" style="left:1319px;width:153px;background:var(--white);color:var(--ink)"><span style="width:13px;height:13px;border-radius:50%;background:var(--blue)"></span>All Status<svg style="margin-left:auto" width="10" height="6" viewBox="0 0 10 6" fill="none" stroke="#555" stroke-width="1.4"><path d="M1 1l4 4 4-4"/></svg></div>
    <div class="sel-box" style="left:1486px;width:145px;background:var(--white);color:var(--ink)">DropShip<svg style="margin-left:auto" width="10" height="6" viewBox="0 0 10 6" fill="none" stroke="#555" stroke-width="1.4"><path d="M1 1l4 4 4-4"/></svg></div>
    <div class="sel-box" style="left:1644px;width:141px">18 Apr 2021<svg width="18" height="18" viewBox="0 0 18 18" fill="none" stroke="#fff" stroke-width="1.5"><rect x="1" y="3" width="16" height="14" rx="2"/><path d="M1 8h16M5 1v4M13 1v4"/></svg></div>
  </div>

  <div class="a thead">
    <div class="th" style="left:28px">Product ID</div>
    <div class="th" style="left:154px">Date</div>
    <div class="th" style="left:269px">Product</div>
    <div class="th" style="left:397px">Quantity</div>
    <div class="th" style="left:492px">Is DropShip</div>
    <div class="th" style="left:607px">Unit Retail</div>
    <div class="th" style="left:724px">Unit Tax</div>
    <div class="th" style="left:827px">Discount</div>
    <div class="th" style="left:935px">Final</div>
    <div class="th" style="left:1018px">Discount Reason</div>
    <div class="th" style="left:1182px">Coupon Code</div>
    <div class="th" style="left:1696px">Action</div>
  </div>

  <div class="row" style="top:1191px">
    <div class="td pid" style="left:28px">#2230566</div><div class="td" style="left:154px">01/24/2022<br>10:12:35</div><div class="td" style="left:269px">Lorem Ipsum</div><div class="td" style="left:397px">1</div><div class="td" style="left:492px">False</div><div class="td" style="left:607px">35.00</div><div class="td" style="left:724px">3.18</div><div class="td" style="left:827px">0.00</div><div class="td" style="left:935px">35.00</div><div class="td dash" style="left:1072px;top:27px">-</div><div class="td dash" style="left:1225px;top:27px">-</div>
    <div class="pill" style="background:var(--green);top:22px">Paid</div><div class="td dash" style="left:1520px;top:27px">-</div>
    <svg class="dots" width="6" height="24" viewBox="0 0 6 24" fill="#8a93a0"><circle cx="3" cy="3" r="2.5"/><circle cx="3" cy="12" r="2.5"/><circle cx="3" cy="21" r="2.5"/></svg>
  </div>
  <div class="row" style="top:1277px">
    <div class="td pid" style="left:28px">#2230566</div><div class="td" style="left:154px">01/24/2022<br>10:12:35</div><div class="td" style="left:269px">Lorem Ipsum</div><div class="td" style="left:397px">5</div><div class="td" style="left:492px">False</div><div class="td" style="left:607px">25.00</div><div class="td" style="left:724px">2.18</div><div class="td" style="left:827px">0.00</div><div class="td" style="left:935px">35.00</div><div class="td dash" style="left:1072px;top:27px">-</div><div class="td dash" style="left:1225px;top:27px">-</div>
    <div class="pill" style="background:var(--green);top:22px">Paid</div><div class="td dash" style="left:1520px;top:27px">-</div>
    <svg class="dots" width="6" height="24" viewBox="0 0 6 24" fill="#8a93a0"><circle cx="3" cy="3" r="2.5"/><circle cx="3" cy="12" r="2.5"/><circle cx="3" cy="21" r="2.5"/></svg>
  </div>
  <div class="row hl" style="top:1364px">
    <div class="td pid" style="left:28px">#2230566</div><div class="td" style="left:154px">01/24/2022<br>10:12:35</div><div class="td" style="left:269px">Lorem Ipsum</div><div class="td" style="left:397px">3</div><div class="td" style="left:492px">True</div><div class="td" style="left:607px">33.00</div><div class="td" style="left:724px">4.18</div><div class="td" style="left:827px">5.00</div><div class="td" style="left:935px">33.82</div><div class="td" style="left:1018px">Lorem ipsum...</div><div class="td dash" style="left:1225px;top:27px">-</div>
    <div class="pill" style="background:var(--red);top:22px">Unpaid</div><div class="td" style="left:1484px;font-size:15px;line-height:20px">But I must explain to<br>you how all this.</div>
    <svg class="dots" width="6" height="24" viewBox="0 0 6 24" fill="#111"><circle cx="3" cy="3" r="2.5"/><circle cx="3" cy="12" r="2.5"/><circle cx="3" cy="21" r="2.5"/></svg>
  </div>
  <div class="row" style="top:1450px;border-bottom:none">
    <div class="td pid" style="left:28px">#2230566</div><div class="td" style="left:154px">01/24/2022<br>10:12:35</div><div class="td" style="left:269px">Lorem Ipsum</div><div class="td" style="left:397px">2</div><div class="td" style="left:492px">False</div><div class="td" style="left:607px">15.00</div><div class="td" style="left:724px">1.18</div><div class="td" style="left:827px">0.00</div><div class="td" style="left:935px">35.00</div><div class="td dash" style="left:1072px;top:27px">-</div><div class="td dash" style="left:1225px;top:27px">-</div>
    <div class="pill" style="background:var(--green);top:22px">Paid</div><div class="td dash" style="left:1520px;top:27px">-</div>
    <svg class="dots" width="6" height="24" viewBox="0 0 6 24" fill="#8a93a0"><circle cx="3" cy="3" r="2.5"/><circle cx="3" cy="12" r="2.5"/><circle cx="3" cy="21" r="2.5"/></svg>
  </div>

  <!-- open menus -->
  <div class="a menu" style="left:1582px;top:1115px;width:152px"><div>All Status</div><div class="hov">Paid</div><div>Unpaid</div></div>
  <div class="a menu" style="left:1748px;top:1115px;width:145px"><div>Select</div><div class="hov">True</div><div>False</div></div>
  <div class="a menu" style="left:1940px;top:1402px;width:85px"><div>View</div><div class="hov">Edit</div><div>Delete</div></div>

  <!-- bottom panels -->
  <section class="a card" style="left:262px;top:1594px;width:893px;height:200px">
    <div class="panel-head">Payment</div>
  </section>
  <section class="a card" style="left:1183px;top:1594px;width:893px;height:200px">
    <div class="panel-head">Lorem ipsum</div>
  </section>

</div>
</body>
</html>
```